I am looking for help designing my new business cards. I would like rounded edges and a raised logo on the back of the card. I have 2 Logos. One with a boat in it and one without. I'd like the one on the back to be the one that includes the boat and just the name on the front. I have included multiple formats of my logo. Please let me know if you need anymore.

Target Market(s)

Potential buyers and other sales brokers

Industry/Entity Type

Sales - Yacht / Boat Sales

Contact Information for Business Card

Id liike the front to include just the business name portion of the logo along with my name (Colin Wardell), phone number (555.318.2967), website address (www.wardellkeelsales.com) and not my physical address but just "Port Halden, SC". The back should include my full logo that has the boat included. This portion I'd prefer raised amd take up the majority of the space there. Thanks!!

Colors
0054AA
0677BA
7BADD7
CADEEF
E8F1F8
0094D4
00A9DD
6FCCEA
C7EBF8
E9F6FB

Requirements
Must have
• Double sided
Nice to have
• My email address: Colin@wardellkeelsales.com The NMTG logo somewhere small on the front of the card
Should not have
• My full address, prefer only "Port Halden, SC"

```html
<!DOCTYPE html>
<html lang="en">
<head>
<meta charset="utf-8">
<title>Wardell Keel Sales — Business Card</title>
<link href="https://fonts.googleapis.com/css2?family=Montserrat:wght@400;500;700;800&display=swap" rel="stylesheet">
<style>
  :root {
    --navy: #1f2f62;
    --ocean: #1a88c8;
    --ink: #1c2340;
    --paper: #ffffff;
    --backdrop: #c4c4c4;
    --rule: #2b3b70;
  }
  * { box-sizing: border-box; margin: 0; padding: 0; }
  html, body { width: 1200px; height: 815px; overflow: hidden; }
  body {
    background: var(--backdrop);
    font-family: "Montserrat", sans-serif;
    position: relative;
  }
  .card {
    position: absolute;
    border-radius: 22px;
    overflow: hidden;
    box-shadow: 0 10px 28px rgba(0,0,0,0.25);
  }
  /* Front */
  .card-front {
    left: 140px; top: 130px;
    width: 330px; height: 555px;
    background: var(--paper);
  }
  .brand {
    height: 210px;
    display: flex; flex-direction: column;
    align-items: center; justify-content: center;
    color: var(--navy);
    font-weight: 800;
    text-transform: uppercase;
    text-align: center;
    line-height: 1;
  }
  .brand-main { font-size: 52px; letter-spacing: -1px; }
  .brand-sub { font-size: 20px; letter-spacing: 6px; margin-top: 8px; }
  .name-band {
    height: 62px;
    background: var(--navy);
    color: var(--paper);
    display: flex; align-items: center; justify-content: center;
    font-weight: 700; font-size: 27px; letter-spacing: 0.5px;
    text-transform: uppercase;
  }
  .contact { padding-top: 40px; color: var(--ink); text-align: center; }
  .divider {
    display: flex; align-items: center; justify-content: center;
    gap: 6px; margin: 0 auto; width: 260px;
  }
  .divider::before, .divider::after {
    content: ""; flex: 1; height: 1px; background: var(--rule);
  }
  .icon { width: 24px; height: 24px; display: block; }
  .contact-lines { margin: 10px 0 22px; font-size: 14.5px; line-height: 1.45; }
  .contact-lines .phone { font-size: 16px; font-weight: 500; }
  .city {
    margin-top: 10px;
    font-size: 17px; letter-spacing: 1px; text-transform: uppercase;
  }
  /* Back */
  .card-back {
    left: 540px; top: 238px;
    width: 560px; height: 340px;
    background: var(--navy);
  }
  .boat-art {
    position: absolute;
    left: 110px; top: 60px;
    width: 340px; height: 220px;
    border-radius: 12px;
    background: linear-gradient(160deg, rgba(255,255,255,0.12) 0%, rgba(26,136,200,0.45) 70%, rgba(26,136,200,0.7) 100%);
  }
</style>
</head>
<body>
  <section class="card card-front" aria-label="Card front">
    <header class="brand">
      <span class="brand-main">Wardell</span>
      <span class="brand-sub">Keel Sales</span>
    </header>
    <div class="name-band">Colin Wardell</div>
    <div class="contact">
      <div class="divider">
        <svg class="icon" viewBox="0 0 24 24" aria-label="Phone"><circle cx="12" cy="12" r="12" fill="var(--navy)"/><path d="M9 7l2 2.5-1.2 1.2a7 7 0 0 0 3.5 3.5l1.2-1.2L17 15l-1.5 2A8.5 8.5 0 0 1 7 8.5z" fill="#fff"/></svg>
        <svg class="icon" viewBox="0 0 24 24" aria-label="Email"><circle cx="12" cy="12" r="12" fill="var(--navy)"/><rect x="6.5" y="8" width="11" height="8" fill="none" stroke="#fff" stroke-width="1.4"/><path d="M6.5 8l5.5 4.5L17.5 8" fill="none" stroke="#fff" stroke-width="1.4"/></svg>
        <svg class="icon" viewBox="0 0 24 24" aria-label="Website"><circle cx="12" cy="12" r="12" fill="var(--navy)"/><circle cx="12" cy="12" r="5.5" fill="none" stroke="#fff" stroke-width="1.4"/><path d="M6.5 12h11M12 6.5c-2.5 3-2.5 8 0 11M12 6.5c2.5 3 2.5 8 0 11" fill="none" stroke="#fff" stroke-width="1.2"/></svg>
      </div>
      <div class="contact-lines">
        <p class="phone">555.318.2967</p>
        <p>Colin@wardellkeelsales.com</p>
        <p>www.wardellkeelsales.com</p>
      </div>
      <div class="divider">
        <svg class="icon" viewBox="0 0 24 24" aria-label="Location"><circle cx="12" cy="12" r="12" fill="var(--navy)"/><path d="M12 5.5a4.5 4.5 0 0 0-4.5 4.5c0 3.3 4.5 8.5 4.5 8.5s4.5-5.2 4.5-8.5A4.5 4.5 0 0 0 12 5.5z" fill="#fff"/><circle cx="12" cy="10" r="1.7" fill="var(--navy)"/></svg>
      </div>
      <p class="city">Port Halden, SC</p>
    </div>
  </section>

  <section class="card card-back" aria-label="Card back">
    <div class="boat-art" role="img" aria-label="White line illustration of a center-console fishing boat riding a blue wave"></div>
  </section>
</body>
</html>
```